Graphic design of trade booth

We have recently rebranded our logo and are looking for a redesign of our trade show booth. We have a template attached to show the dimensions.

The booth should have no other text on it except for our logo. We'd like for it to be stylized in a way that conforms to the new logo.

(Please note that our web site is not yet updated with the new logo so don't go there for inspiration.)

Attached: the new logo as well as the template for the booth layout.
Updates

All - please note that we may be switching our booth dimensions. We will have a final answer by tomorrow, March 20. In the event that we do switch, we will:

• post the new dimensions
• extend the competition
• add $$ to the award

Apologize for this, we are receiving some late-breaking information. Stay tuned and thanks for your interest. 

Hello Designers!

First of all, thank you very much for all your submission, and patience, as I know we have changed this project a little bit. Unfortunately, we need to make another change. We realize that many of you have invested time and energy into this project, and for that we truly apologize. In leu of this, we have added an additional $150 to this project - $100 additional for second place, and $50 additional for first place.

Here are the details for our new Banner project:
Please do not hesitate to let us know if you have any questions, etc... And again, we truly apologize for all the changes and updates to this project. Thanks for your participation! 

Target Market(s)

Scientists, executives in the life sciences information space. Rather boring and dull creatures who take themselves rather seriously.

Industry/Entity Type

Graphic Design

```html
<!DOCTYPE html>
<html lang="en">
<head>
<meta charset="utf-8">
<title>HelixSeek Banner</title>
<link rel="stylesheet" href="https://fonts.googleapis.com/css2?family=Poppins:wght@600&display=swap">
<style>
  :root {
    --bg: #ffffff;
    --brand-blue: #0a8fc6;
    --icon-grey: #3d3d3d;
    --faint-grey: #eeeeee;
    --faint-blue: #e4f2f9;
  }
  html, body {
    margin: 0;
    padding: 0;
    overflow: hidden;
    background: var(--bg);
  }
  .banner {
    position: relative;
    width: 700px;
    height: 1200px;
    overflow: hidden;
    background: var(--bg);
    font-family: "Poppins", "Century Gothic", sans-serif;
  }
  .backdrop-circle {
    position: absolute;
    left: 428px;
    top: 945px;
    width: 400px;
    height: 400px;
    border-radius: 50%;
    background: var(--faint-blue);
  }
  .feature {
    position: absolute;
    display: flex;
    align-items: center;
    gap: 22px;
    margin: 0;
  }
  .feature-label {
    color: var(--brand-blue);
    font-size: 68px;
    font-weight: 600;
    line-height: 1;
    letter-spacing: -1px;
  }
  .feature-icon {
    fill: var(--icon-grey);
    flex: none;
  }
  .feature--search    { left: 176px; top: 140px; }
  .feature--analysis  { left: 156px; top: 275px; }
  .feature--content   { left: 158px; top: 436px; }
  .feature--present   { left: 119px; top: 600px; }
  .feature--export    { left: 119px; top: 738px; }

  .brand {
    position: absolute;
    left: 70px;
    top: 1072px;
    display: flex;
    align-items: center;
    gap: 16px;
    color: var(--faint-grey);
    font-size: 62px;
    font-weight: 600;
    letter-spacing: -1px;
  }
  .brand-dot {
    width: 78px;
    height: 78px;
    border-radius: 50%;
    background: var(--faint-grey);
  }
</style>
</head>
<body>
<main class="banner">
  <div class="backdrop-circle"></div>

  <h2 class="feature feature--search">
    <span class="feature-label">Search</span>
    <svg class="feature-icon" width="76" height="76" viewBox="0 0 76 76" aria-hidden="true">
      <circle cx="30" cy="30" r="23" fill="none" stroke="#3d3d3d" stroke-width="8"/>
      <line x1="47" y1="47" x2="70" y2="70" stroke="#3d3d3d" stroke-width="10" stroke-linecap="round"/>
    </svg>
  </h2>

  <h2 class="feature feature--analysis">
    <span class="feature-label">Analysis</span>
    <svg class="feature-icon" width="84" height="92" viewBox="0 0 84 92" aria-hidden="true">
      <g transform="translate(33 33)">
        <g>
          <rect x="-6" y="-33" width="12" height="66" rx="2"/>
          <rect x="-6" y="-33" width="12" height="66" rx="2" transform="rotate(45)"/>
          <rect x="-6" y="-33" width="12" height="66" rx="2" transform="rotate(90)"/>
          <rect x="-6" y="-33" width="12" height="66" rx="2" transform="rotate(135)"/>
        </g>
        <circle r="24"/>
        <circle r="9" fill="#fff"/>
      </g>
      <g transform="translate(67 75)">
        <rect x="-3" y="-15" width="6" height="30" rx="1"/>
        <rect x="-3" y="-15" width="6" height="30" rx="1" transform="rotate(45)"/>
        <rect x="-3" y="-15" width="6" height="30" rx="1" transform="rotate(90)"/>
        <rect x="-3" y="-15" width="6" height="30" rx="1" transform="rotate(135)"/>
        <circle r="11"/>
        <circle r="4.5" fill="#fff"/>
      </g>
    </svg>
  </h2>

  <h2 class="feature feature--content">
    <span class="feature-label">Content</span>
    <svg class="feature-icon" width="64" height="78" viewBox="0 0 64 78" aria-hidden="true">
      <g fill="#fff" stroke="#3d3d3d" stroke-width="2.5">
        <rect x="22" y="2" width="38" height="54"/>
        <rect x="12" y="10" width="38" height="56"/>
        <rect x="2" y="18" width="38" height="56"/>
      </g>
      <g stroke="#3d3d3d" stroke-width="2.5">
        <line x1="9" y1="32" x2="33" y2="32"/>
        <line x1="9" y1="40" x2="33" y2="40"/>
        <line x1="9" y1="48" x2="33" y2="48"/>
        <line x1="9" y1="56" x2="33" y2="56"/>
        <line x1="9" y1="64" x2="27" y2="64"/>
      </g>
    </svg>
  </h2>

  <h2 class="feature feature--present">
    <span class="feature-label">Reporting</span>
    <svg class="feature-icon" width="64" height="78" viewBox="0 0 64 78" aria-hidden="true">
      <rect x="28" y="0" width="6" height="6"/>
      <rect x="0" y="6" width="62" height="5"/>
      <rect x="3" y="13" width="56" height="36"/>
      <circle cx="18" cy="31" r="10" fill="#fff"/>
      <path d="M18 31 L18 21 A10 10 0 0 1 28 31 Z" fill="#3d3d3d"/>
      <g fill="#fff">
        <rect x="33" y="20" width="20" height="3"/>
        <rect x="33" y="26" width="20" height="3"/>
        <rect x="33" y="32" width="20" height="3"/>
        <rect x="33" y="38" width="20" height="3"/>
      </g>
      <g stroke="#3d3d3d" stroke-width="3">
        <line x1="31" y1="49" x2="31" y2="76"/>
        <line x1="28" y1="49" x2="18" y2="76"/>
        <line x1="34" y1="49" x2="44" y2="76"/>
        <line x1="22" y1="64" x2="40" y2="64"/>
      </g>
    </svg>
  </h2>

  <h2 class="feature feature--export">
    <span class="feature-label">Reporting</span>
    <svg class="feature-icon" width="62" height="46" viewBox="0 0 62 46" aria-hidden="true">
      <path d="M12 8 H20 V14 H15 L7 28 H20 L24 34 H38 L42 28 H55 L47 14 H42 V8 H50 L62 28 V42 Q62 46 58 46 H4 Q0 46 0 42 V28 Z"/>
      <rect x="28" y="4" width="6" height="14"/>
      <path d="M22 16 H40 L31 26 Z"/>
    </svg>
  </h2>

  <div class="brand" aria-label="HelixSeek">
    <span class="brand-dot"></span>
    <span class="brand-name">HelixSeek</span>
  </div>
</main>
</body>
</html>
```